Interior Design business card design

I am an interior decorator - dont want to specify decorating more just design.
Want organic looking logo - charcoal and white - with touch of lime green.
Like the idea of some sort of spiral in corner but writing in a line
want lower case, tildamarchetti as one and designs in different font underneath. Maybe using t and m as logo.
More modern than traditional. My clients are mid to top end residential

Target Market(s)

medium to top end homeowners

Industry/Entity Type

Residential

Contact Information for Business Card

Tilda Marchetti Designs
58 Kellaway ave
Pemberly 2190 NSW
Tel 0417268914
tildamarchetti@velnaro.com.au

Logo Text

Tilda Marchetti Designs

Logo styles of interest
Abstract Logo
Lettermark Logo
Requirements
Must have
• Name address ph and e mail
Nice to have
• Contemporary
smart but organic
Should not have
• no traditional fonts

```html
<!DOCTYPE html>
<html lang="en">
<head>
<meta charset="utf-8">
<title>Tilda Marchetti Designs – Business Card</title>
<link rel="stylesheet" href="https://fonts.googleapis.com/css2?family=Titillium+Web:wght@300&display=swap">
<style>
  :root {
    --charcoal: #1b2627;
    --slate-band: #6f8f90;
    --paper: #ffffff;
    --lime: #8fe635;
    --ink-light: #ffffff;
  }
  html, body {
    margin: 0;
    padding: 0;
    width: 1200px;
    height: 693px;
    overflow: hidden;
    background: var(--paper);
  }
  .card {
    position: relative;
    width: 1200px;
    height: 693px;
    background: var(--paper);
    font-family: "Titillium Web", "Helvetica Neue", Arial, sans-serif;
    font-weight: 300;
    color: var(--ink-light);
  }
  .card__backdrop {
    position: absolute;
    inset: 0;
    display: block;
  }
  .brand {
    position: absolute;
    left: 150px;
    top: 120px;
    width: 310px;
    text-align: center;
  }
  .brand__ring {
    display: block;
    margin: 0 auto 34px;
  }
  .brand__name,
  .brand__tagline {
    margin: 0;
    font-weight: 300;
    color: var(--ink-light);
    line-height: 1.1;
  }
  .brand__name {
    font-size: 46px;
    letter-spacing: 0.5px;
  }
  .brand__tagline {
    font-size: 40px;
    margin-top: 4px;
  }
  .contact {
    position: absolute;
    left: 600px;
    top: 252px;
    margin: 0;
    font-style: normal;
    font-size: 28.5px;
    line-height: 40px;
    letter-spacing: 0.2px;
  }
  .contact__line {
    display: block;
    white-space: nowrap;
  }
</style>
</head>
<body>
  <div class="card">
    <svg class="card__backdrop" width="1200" height="693" viewBox="0 0 1200 693" aria-hidden="true">
      <path d="M0 0 H1200 V570 Q600 690 0 560 Z" fill="var(--slate-band)"/>
      <path d="M0 0 H1200 V540 Q600 665 0 538 Z" fill="var(--charcoal)"/>
    </svg>

    <div class="brand">
      <svg class="brand__ring" width="150" height="150" viewBox="0 0 150 150" aria-hidden="true">
        <circle cx="75" cy="75" r="66" fill="none" stroke="var(--lime)" stroke-width="12"/>
      </svg>
      <p class="brand__name">tildamarchetti</p>
      <p class="brand__tagline">Designs</p>
    </div>

    <address class="contact">
      <span class="contact__line">Tilda Marchetti Designs</span>
      <span class="contact__line">58 Kellaway ave Pemberly 2190 NSW</span>
      <span class="contact__line">Tel 0417268914</span>
      <span class="contact__line">tildamarchetti@velnaro.com.au</span>
    </address>
  </div>
</body>
</html>
```